Business Card Design

We have our logo and everything in place. Looking to have a layout for our new business cards designed. These will be printed with a matte finish, possibly rounded corners, and looking to incorporate some cool spot UV layers into the design.

Ive uploaded the existing card front and back as well as our logo.

Card Size Will Be 3.5" x 2"

```html
<!DOCTYPE html>
<html lang="en">
<head>
<meta charset="utf-8">
<title>Cedarline Deck and Rail – Business Cards</title>
<link href="https://fonts.googleapis.com/css2?family=Crimson+Text:ital,wght@0,400;0,600;1,400&display=swap" rel="stylesheet">
<style>
  :root {
    --stage: #3a3330;
    --card-black: #161616;
    --card-black-soft: #1e1e1e;
    --uv-gloss: #2a2a2a;
    --swoosh-grey: #6e6c6a;
    --swoosh-light: #b9b9b9;
    --ink-white: #f4f4f4;
    --serif: "Crimson Text", Georgia, serif;
  }
  * { box-sizing: border-box; margin: 0; padding: 0; }
  html, body { width: 1200px; height: 716px; overflow: hidden; }
  body { background: var(--stage); font-family: var(--serif); }

  .canvas { position: relative; width: 1200px; height: 716px; }

  .card {
    position: absolute;
    width: 520px; height: 297px;
    border-radius: 10px;
    overflow: hidden;
    background: linear-gradient(160deg, var(--card-black-soft), var(--card-black));
    box-shadow: 0 10px 26px rgba(0,0,0,.45);
  }
  .card--front { left: 40px; top: 210px; }
  .card--back  { left: 640px; top: 210px; }

  /* Spot UV wordmark on the front */
  .uv-mark {
    position: absolute; left: 0; right: 0; top: 96px;
    text-align: center; color: var(--uv-gloss);
  }
  .uv-mark__name { font-size: 64px; font-weight: 600; line-height: 1; }
  .uv-mark__tag { font-size: 15px; font-weight: 600; letter-spacing: 3px; margin-top: 6px; }

  /* Back */
  .back-art { position: absolute; inset: 0; width: 100%; height: 100%; }

  .brand {
    position: absolute; left: 34px; top: 46px;
    color: var(--ink-white); font-weight: 600;
    display: flex; align-items: flex-start; gap: 10px;
  }
  .brand__dot { width: 10px; height: 10px; background: var(--ink-white); margin-top: 16px; }
  .brand__name { font-size: 46px; line-height: 1; }
  .brand__tag { font-size: 12px; letter-spacing: 2px; margin-top: 4px; padding-left: 60px; }

  .person { position: absolute; right: 30px; top: 60px; text-align: right; color: var(--ink-white); }
  .person__name { font-size: 24px; letter-spacing: 1.5px; }
  .person__role { font-size: 14px; font-style: italic; margin-top: 2px; }

  .contact {
    position: absolute; right: 22px; bottom: 20px;
    list-style: none; color: var(--ink-white);
    font-size: 15px; line-height: 1.35; text-align: right;
  }
  .contact li { display: flex; justify-content: flex-end; align-items: center; gap: 8px; }
  .contact svg { width: 12px; height: 12px; flex: none; }
</style>
</head>
<body>
<main class="canvas">

  <section class="card card--front" aria-label="Card front">
    <div class="uv-mark">
      <div class="uv-mark__name">Cedarline</div>
      <div class="uv-mark__tag">DECK AND RAIL</div>
    </div>
  </section>

  <section class="card card--back" aria-label="Card back">
    <svg class="back-art" viewBox="0 0 520 297" preserveAspectRatio="none" aria-hidden="true">
      <path d="M0,178 C120,150 230,250 520,222 L520,297 L0,297 Z" fill="var(--swoosh-grey)"/>
      <path d="M0,150 C130,128 240,232 520,196" fill="none" stroke="var(--swoosh-light)" stroke-width="7"/>
      <path d="M0,164 C140,140 250,240 520,208" fill="none" stroke="#ffffff" stroke-width="3"/>
    </svg>

    <div class="brand">
      <span class="brand__dot"></span>
      <div>
        <div class="brand__name">Cedarline</div>
        <div class="brand__tag">DECK AND RAIL</div>
      </div>
    </div>

    <div class="person">
      <div class="person__name">Daniel Mercer</div>
      <div class="person__role">President</div>
    </div>

    <ul class="contact">
      <li>555.014.2290
        <svg viewBox="0 0 12 12" aria-label="Phone"><path d="M2 1h2.5l1 3-1.5 1a6 6 0 0 0 3 3l1-1.5 3 1V11c-5 0-9-4-9-9z" fill="#fff"/></svg>
      </li>
      <li>cedarlinedeckandrail@mail.com
        <svg viewBox="0 0 12 12" aria-label="Email"><rect x="1" y="2.5" width="10" height="7" fill="none" stroke="#fff"/><path d="M1 2.5l5 4 5-4" fill="none" stroke="#fff"/></svg>
      </li>
      <li>cedarlinedeckandrail.com
        <svg viewBox="0 0 12 12" aria-label="Website"><circle cx="6" cy="6" r="5" fill="none" stroke="#fff"/><path d="M1 6h10M6 1c-2.5 3-2.5 7 0 10M6 1c2.5 3 2.5 7 0 10" fill="none" stroke="#fff" stroke-width=".8"/></svg>
      </li>
    </ul>
  </section>

</main>
</body>
</html>
```